Business card design for industrial spray painting - startup business

Design the layout of our new business card using the logo we have provided.

We want the card to be matt black in colour.

We only want our logo and slogan on the face side.

Because the card is black we would like the slogan WE PAINT ANYTHING! to be in white.

We want our information on the rear side.

I would like my name in blue matching the blue in the logo.

The remainder of the information should be in grey to match the grey in the logo.

The overall finish should look minimal, clean and slick.

Our business is industrlal and of a masculine nature.

Target Market(s)

industrial and mining companies

Contact Information for Business Card

(front of card – matt black)
insert logo here:
insert this tag line: WE PAINT ANYTHING!

--------------------------------------------------------------------------------------------------------------

(back of card – matt black)
Dorian Kestle
Paint and Coatings Specialist
47 Millbrook Avenue, Ferndale Rise WA 6148
M: +61 437 281 914
T: +61 8 555 7318
E: dorian@coatlynx.co
W: www.coatlynx.co

Font styles to use
Sans Serif

Colors
000000
0455a3

Requirements
Must have
• clean, slick minimalist look. Masculine as we deal mostly with industrial spray painting

```html
<!DOCTYPE html>
<html lang="en">
<head>
<meta charset="utf-8">
<title>Coatlynx — Business Card</title>
<link rel="stylesheet" href="https://fonts.googleapis.com/css2?family=Michroma&family=Roboto:wght@400;700&display=swap">
<style>
  :root {
    --backdrop: #1c1c1e;
    --card: #0b0b0c;
    --blue: #1d7fcf;
    --grey: #8e8f91;
    --rule: #55575a;
    --white: #ffffff;
  }
  * { margin: 0; padding: 0; box-sizing: border-box; }
  html, body {
    width: 1200px; height: 1200px; overflow: hidden;
    background: var(--backdrop);
  }
  .canvas {
    position: relative; width: 1200px; height: 1200px;
    display: flex; flex-direction: column; align-items: center; justify-content: center; gap: 60px;
  }
  .card {
    position: relative; width: 820px; height: 500px;
    background: var(--card);
    box-shadow: 0 18px 40px rgba(0,0,0,.55);
  }
  .brand {
    display: flex; align-items: center; gap: 18px;
    font-family: "Michroma", sans-serif; color: var(--blue);
    letter-spacing: 2px; white-space: nowrap;
  }
  .brand-mark { width: 30px; height: 30px; background: var(--blue); flex: none; }

  /* Front */
  .card-front .brand {
    position: absolute; top: 180px; left: 0; right: 0; justify-content: center;
    font-size: 46px;
  }
  .card-front .brand-mark { width: 40px; height: 40px; }
  .slogan {
    position: absolute; top: 330px; left: 0; right: 0; text-align: center;
    font-family: "Michroma", sans-serif; font-size: 17px; letter-spacing: 2px;
    color: var(--white);
  }

  /* Back */
  .card-back .brand { position: absolute; top: 75px; left: 110px; font-size: 34px; }
  .holder { position: absolute; top: 170px; left: 90px; font-family: "Roboto", sans-serif; }
  .holder-name { font-size: 32px; font-weight: 700; color: var(--blue); line-height: 1.1; }
  .holder-role { font-size: 22px; color: var(--grey); margin-top: 6px; }
  .divider { position: absolute; top: 262px; left: 80px; width: 660px; height: 1px; background: var(--rule); }
  .contacts {
    position: absolute; top: 282px; left: 80px; list-style: none;
    font-family: "Roboto", sans-serif; font-size: 21px; color: var(--grey);
  }
  .contacts li { display: flex; align-items: center; gap: 14px; height: 34px; white-space: nowrap; }
  .contacts svg { width: 20px; height: 20px; flex: none; }
  .address {
    position: absolute; top: 350px; right: 80px; text-align: right;
    font-family: "Roboto", sans-serif; font-style: normal; font-size: 22px; line-height: 34px; color: var(--grey);
    white-space: nowrap;
  }
</style>
</head>
<body>
<main class="canvas">
  <section class="card card-front" aria-label="Card front">
    <div class="brand"><span class="brand-mark"></span><span class="brand-name">COATLYNX</span></div>
    <p class="slogan">WE PAINT ANYTHING!</p>
  </section>

  <section class="card card-back" aria-label="Card back">
    <div class="brand"><span class="brand-mark"></span><span class="brand-name">COATLYNX</span></div>
    <div class="holder">
      <p class="holder-name">Dorian Kestle</p>
      <p class="holder-role">Paint and Coatings Specialist</p>
    </div>
    <div class="divider"></div>
    <ul class="contacts">
      <li>
        <svg viewBox="0 0 20 20" fill="none" stroke="var(--blue)" stroke-width="2"><rect x="5" y="2" width="10" height="16" rx="2"/><line x1="8" y1="15" x2="12" y2="15"/></svg>
        +61 437 281 914
      </li>
      <li>
        <svg viewBox="0 0 20 20" fill="var(--blue)"><path d="M5 2l3 4-2 2c1 2.5 3.5 5 6 6l2-2 4 3-2 3C9 17 3 11 2 4z"/></svg>
        +61 8 555 7318
      </li>
      <li>
        <svg viewBox="0 0 20 20" fill="none" stroke="var(--blue)" stroke-width="2"><rect x="2" y="4" width="16" height="12"/><polyline points="2,4 10,11 18,4"/></svg>
        dorian@coatlynx.co
      </li>
      <li>
        <svg viewBox="0 0 20 20" fill="none" stroke="var(--blue)" stroke-width="1.6"><circle cx="10" cy="10" r="8"/><ellipse cx="10" cy="10" rx="3.5" ry="8"/><line x1="2" y1="10" x2="18" y2="10"/><line x1="3.5" y1="6" x2="16.5" y2="6"/><line x1="3.5" y1="14" x2="16.5" y2="14"/></svg>
        www.coatlynx.co
      </li>
    </ul>
    <address class="address">47 Millbrook Avenue<br>Ferndale Rise WA 6148</address>
  </section>
</main>
</body>
</html>
```